Business Card Design

We require a business card design for a law firm, our signature colours are maroon and cream. Our slogan is "From our family to yours", we would like the cards to be professional however feminine at the same time.

Industry/Entity Type

Business

Contact Information for Business Card

Helena Brockett & Associates Lawyers & Conveyancers, Helena Brockett LL.B. Principal Solicitor, 17 Thornbury Street, Kelvale NSW 2239

Logo styles of interest
Emblem Logo
Abstract Logo
Wordmark Logo

```html
<!DOCTYPE html>
<html lang="en">
<head>
<meta charset="utf-8">
<title>Helena Brockett &amp; Associates – Business Card</title>
<link rel="stylesheet" href="https://fonts.googleapis.com/css2?family=Noto+Serif:wght@400&display=swap">
<style>
  :root {
    --backdrop: #d9d9d9;
    --card-magenta: #c42a6c;
    --card-magenta-deep: #a81f5b;
    --cream: #f0dcb2;
  }
  html, body {
    margin: 0;
    padding: 0;
    width: 1200px;
    height: 900px;
    overflow: hidden;
    background: var(--backdrop);
  }
  .canvas {
    position: relative;
    width: 1200px;
    height: 900px;
    display: flex;
    align-items: center;
    justify-content: center;
  }
  .business-card {
    position: relative;
    width: 880px;
    height: 503px;
    background: linear-gradient(160deg, var(--card-magenta) 0%, var(--card-magenta-deep) 100%);
    box-shadow: 0 14px 34px rgba(0, 0, 0, 0.25);
    overflow: hidden;
    font-family: "Noto Serif", "DejaVu Serif", Georgia, serif;
    color: var(--cream);
    text-align: center;
  }
  .card-content {
    position: relative;
    padding-top: 62px;
  }
  .firm-mark {
    display: flex;
    flex-direction: column;
    align-items: center;
    gap: 10px;
  }
  .firm-mark__dot {
    width: 54px;
    height: 54px;
    border-radius: 50%;
    background: var(--cream);
  }
  .firm-mark__name {
    font-size: 21px;
    line-height: 1.2;
    margin: 0;
  }
  .firm-mark__name span { display: block; font-size: 14px; }
  .slogan {
    margin: 28px 0 10px;
    font-size: 24px;
    letter-spacing: 0.5px;
  }
  .divider {
    display: block;
    margin: 0 auto 32px;
  }
  .contact-lines {
    font-size: 21px;
    line-height: 1.55;
    margin: 0;
  }
</style>
</head>
<body>
  <main class="canvas">
    <section class="business-card" aria-label="Business card for Helena Brockett &amp; Associates">
      <div class="card-content">
        <div class="firm-mark">
          <div class="firm-mark__dot" aria-hidden="true"></div>
          <p class="firm-mark__name">Helena Brockett &amp; Associates<span>Lawyers</span></p>
        </div>
        <p class="slogan">FROM OUR FAMILY TO YOURS</p>
        <svg class="divider" width="340" height="14" viewBox="0 0 340 14" aria-hidden="true">
          <line x1="6" y1="7" x2="334" y2="7" stroke="var(--cream)" stroke-width="2"/>
          <circle cx="170" cy="7" r="5" fill="var(--cream)"/>
        </svg>
        <p class="contact-lines">
          Helena Brockett &amp; Associates Lawyers &amp; Conveyancers,<br>
          Helena Brockett LL.B.<br>
          Principal Solicitor, 17 Thornbury Street, Kelvale NSW 2239
        </p>
      </div>
    </section>
  </main>
</body>
</html>
```